Night Dresses business cards business requirers

We are a new company initiating Mexico operations. Our core business is Night woman dress (both formal and party dress) for rent. Gownhaven is the name of the company. ITS Gownhaven form by two word. The dress word and topia (Utopic) so the place Gownhaven Means That You cant get the ideal, perfect and unique dress for your event. So we would like a modern, very creative, and attractive business card.

Industry/Entity Type

Womens Clothing

Contact Information for Business Card

Rounded Borders, two faces

Requirements
Must have
• Rounded borders, logo and slogan, modern, glam, attractive design
Should not have
• modern design classic or not

```html
<!DOCTYPE html>
<html lang="en">
<head>
<meta charset="utf-8">
<title>Gownhaven Business Card</title>
<link rel="stylesheet" href="https://fonts.googleapis.com/css2?family=Open+Sans:wght@400;600;700&display=swap">
<style>
  :root {
    --backdrop: #e9e7ea;
    --card-dark: #262527;
    --card-light: #ffffff;
    --accent: #b2549c;
    --ink: #1f1f1f;
    --ink-light: #f4f4f4;
    --ink-muted: #bdbbbf;
    --shadow: rgba(0, 0, 0, 0.18);
  }
  * { box-sizing: border-box; margin: 0; padding: 0; }
  html, body {
    width: 1200px;
    height: 1000px;
    overflow: hidden;
    background: var(--backdrop);
    font-family: "Open Sans", sans-serif;
  }
  .stage {
    position: relative;
    width: 1200px;
    height: 1000px;
  }
  .card {
    position: absolute;
    left: 280px;
    width: 640px;
    height: 366px;
    border-radius: 28px;
    box-shadow: 0 14px 34px var(--shadow);
    overflow: hidden;
  }
  .card-front { top: 92px; background: var(--card-dark); }
  .card-back { top: 542px; background: var(--card-light); }

  /* Front */
  .brand {
    position: absolute;
    left: 0;
    right: 0;
    top: 138px;
    text-align: center;
  }
  .brand-name {
    display: block;
    color: var(--ink-light);
    font-weight: 400;
    font-size: 38px;
    letter-spacing: 7px;
    line-height: 1;
  }
  .brand-tagline {
    display: block;
    margin-top: 16px;
    color: var(--ink-muted);
    font-weight: 400;
    font-size: 15px;
    letter-spacing: 2px;
  }

  /* Back */
  .person {
    position: absolute;
    left: 80px;
    top: 160px;
    width: 166px;
    text-align: right;
  }
  .person-name {
    color: var(--accent);
    font-weight: 700;
    font-size: 30px;
    line-height: 1.1;
    white-space: nowrap;
  }
  .person-role {
    color: var(--ink);
    font-weight: 600;
    font-size: 16px;
    margin-top: 2px;
  }
  .contact-list {
    position: absolute;
    left: 330px;
    top: 100px;
    list-style: none;
  }
  .contact-list li {
    display: flex;
    align-items: center;
    gap: 12px;
    font-size: 17px;
    color: var(--ink);
    line-height: 26px;
  }
  .contact-list svg { width: 15px; height: 15px; fill: var(--accent); flex: none; }
  .site-name { color: var(--accent); }
  .address {
    position: absolute;
    right: 70px;
    bottom: 48px;
    display: flex;
    align-items: center;
    gap: 12px;
    font-size: 17px;
    color: var(--ink);
  }
  .address svg { width: 16px; height: 16px; fill: var(--accent); }
</style>
</head>
<body>
<main class="stage">
  <section class="card card-front" aria-label="Card front">
    <div class="brand">
      <span class="brand-name">GOWNHAVEN</span>
      <span class="brand-tagline">Evening gowns on loan</span>
    </div>
  </section>

  <section class="card card-back" aria-label="Card back">
    <div class="person">
      <p class="person-name">LENA CRUZ</p>
      <p class="person-role">CEO/FOUNDER</p>
    </div>
    <ul class="contact-list">
      <li>
        <svg viewBox="0 0 16 16"><path d="M4 1l2.5 3-1.5 2a9 9 0 0 0 5 5l2-1.5 3 2.5-1.5 2.5C7 14.5 1.5 9 1.5 2.5z"/></svg>
        000 000 0000
      </li>
      <li>
        <svg viewBox="0 0 16 16"><path d="M1 5c2-3 12-3 14 0l-1 2-3-1V4.5c-2-.6-4-.6-6 0V6L2 7zM3 9h10l1 5H2z"/></svg>
        000 000 0000
      </li>
      <li>
        <svg viewBox="0 0 16 16"><path d="M1 3h14v10H1zM2 4l6 5 6-5v1l-6 5-6-5z" fill-rule="evenodd"/></svg>
        info@lenacruz.com
      </li>
      <li>
        <svg viewBox="0 0 16 16"><path d="M6.5 1a5.5 5.5 0 1 1 0 11 5.5 5.5 0 0 1 0-11zm0 2a3.5 3.5 0 1 0 0 7 3.5 3.5 0 0 0 0-7zM10 11l1.5-1.5L15 13l-1.5 1.5z" fill-rule="evenodd"/></svg>
        <span>www.<span class="site-name">yoursitename</span>.com</span>
      </li>
    </ul>
    <div class="address">
      <svg viewBox="0 0 16 16"><path d="M15 1L1 7l6 2 2 6z"/></svg>
      Your Street address, Singapore-1200
    </div>
  </section>
</main>
</body>
</html>
```